【 概要 】 私が運営しているVidlarkチャンネルのサムネイル制作です。 https://www.vidlark-stream.example/channel/UCxq7RmTbn3KwdLpAe92HfZo?view_as=subscriber 【 依頼内容 】 ・サイズ: 横1,280 × 縦720px ・作成数: 1種類 ・利用用途:Vidlark 【 デザインイメージ 】 ・雰囲気:色数は抑えつつ、多少インパクトを持たせたデザインでお願いします。 【素材】 写真は1点用意しています。 【入れていただきたいテキスト】 ◆大キャッチ◆ 激旨タイ食堂で プチ炎上した伝説の動画 |
こちらの要望通り、色数をおさえつつインパクトのある作品に仕上げていただきました。
たくさんのご提案ありがとうございました。
今後も同様のお仕事を発注してまいりますので、また機会がありましたらよろしくお願いいたします。

```html
<!DOCTYPE html>
<html lang="ja">
<head>
<meta charset="utf-8">
<title>激旨タイ食堂でプチ炎上した伝説の動画</title>
<link rel="stylesheet" href="https://fonts.googleapis.com/css2?family=Noto+Sans+JP:wght@900&display=swap">
<style>
  :root{
    --scene-light:#c9c2b4;
    --scene-mid:#8a7f72;
    --scene-dark:#3a3430;
    --flame-core:#ffd23a;
    --flame-mid:#ff7a12;
    --flame-edge:#c81e05;
    --ink:#1a0d08;
    --white:#ffffff;
    --red:#e4201a;
    --gold-top:#fff36a;
    --gold-bottom:#f08a00;
    --streak:#e9e9e9;
  }
  html,body{margin:0;padding:0;overflow:hidden;background:#000;}
  .thumbnail{
    position:relative;width:1200px;height:676px;overflow:hidden;
    font-family:"Noto Sans JP",sans-serif;
  }
  .scene-photo{
    position:absolute;inset:0;
    background:
      radial-gradient(ellipse 30% 55% at 20% 70%, #2a2422 0%, rgba(42,36,34,0) 70%),
      radial-gradient(ellipse 25% 50% at 77% 72%, #b5342a 0%, rgba(181,52,42,0) 70%),
      linear-gradient(180deg,var(--scene-light) 0%,var(--scene-mid) 55%,var(--scene-dark) 100%);
  }
  .flames{
    position:absolute;inset:0;
    background:
      radial-gradient(ellipse 22% 30% at 4% 6%, var(--flame-core) 0%, var(--flame-mid) 40%, rgba(200,30,5,.6) 65%, rgba(200,30,5,0) 100%),
      radial-gradient(ellipse 20% 26% at 98% 2%, var(--flame-mid) 0%, rgba(200,30,5,.5) 60%, rgba(200,30,5,0) 100%),
      radial-gradient(ellipse 26% 32% at 96% 100%, var(--flame-core) 0%, var(--flame-mid) 40%, rgba(200,30,5,.6) 65%, rgba(200,30,5,0) 100%),
      radial-gradient(ellipse 12% 14% at 16% 96%, var(--flame-mid) 0%, rgba(200,30,5,0) 100%);
  }
  .speed-lines{position:absolute;inset:0;}
  .headline{position:absolute;inset:0;}
  .headline text{font-family:"Noto Sans JP",sans-serif;font-weight:900;}
</style>
</head>
<body>
<main class="thumbnail">
  <div class="scene-photo" role="img" aria-label="タイの屋台食堂で麺料理を前にした男性と笑顔の女性の写真"></div>
  <div class="flames" role="img" aria-label="画面の角から燃え上がる炎"></div>

  <svg class="speed-lines" width="1200" height="676" viewBox="0 0 1200 676" aria-hidden="true">
    <g stroke="var(--streak)" stroke-linecap="round" opacity=".8">
      <line x1="0" y1="150" x2="110" y2="150" stroke-width="6"/>
      <line x1="0" y1="190" x2="70" y2="190" stroke-width="4"/>
      <line x1="0" y1="250" x2="140" y2="250" stroke-width="8"/>
      <line x1="0" y1="310" x2="90" y2="310" stroke-width="5"/>
      <line x1="0" y1="360" x2="120" y2="360" stroke-width="6"/>
      <line x1="0" y1="420" x2="80" y2="420" stroke-width="4"/>
      <line x1="0" y1="480" x2="130" y2="480" stroke-width="7"/>
      <line x1="0" y1="540" x2="95" y2="540" stroke-width="5"/>
      <line x1="960" y1="30" x2="1200" y2="30" stroke-width="5"/>
      <line x1="1020" y1="70" x2="1200" y2="70" stroke-width="7"/>
      <line x1="990" y1="110" x2="1200" y2="110" stroke-width="4"/>
      <line x1="1060" y1="150" x2="1200" y2="150" stroke-width="6"/>
    </g>
  </svg>

  <svg class="headline" width="1200" height="676" viewBox="0 0 1200 676">
    <defs>
      <linearGradient id="gold" x1="0" y1="0" x2="0" y2="1">
        <stop offset="0" stop-color="var(--gold-top)"/>
        <stop offset="1" stop-color="var(--gold-bottom)"/>
      </linearGradient>
    </defs>
    <title>激旨タイ食堂で プチ炎上した伝説の動画</title>

    <g transform="rotate(-9 660 170)">
      <text x="360" y="210" font-size="92" fill="none" stroke="var(--ink)" stroke-width="22" stroke-linejoin="round" aria-hidden="true">激旨タイ食堂で</text>
      <text x="360" y="210" font-size="92" fill="var(--white)" stroke="var(--red)" stroke-width="8" stroke-linejoin="round" paint-order="stroke">激旨タイ食堂で</text>
    </g>

    <g transform="rotate(-5 440 370)">
      <text x="110" y="420" font-size="112" fill="none" stroke="var(--ink)" stroke-width="26" stroke-linejoin="round" aria-hidden="true">プチ炎上した</text>
      <text x="110" y="420" font-size="112" fill="var(--red)" stroke="var(--white)" stroke-width="10" stroke-linejoin="round" paint-order="stroke">プチ炎上した</text>
    </g>

    <g>
      <text x="300" y="615" font-size="166" fill="none" stroke="var(--white)" stroke-width="30" stroke-linejoin="round" aria-hidden="true">伝説の動画</text>
      <text x="300" y="615" font-size="166" fill="url(#gold)" stroke="var(--ink)" stroke-width="14" stroke-linejoin="round" paint-order="stroke">伝説の動画</text>
    </g>
  </svg>
</main>
</body>
</html>
```